Kiswa Design

We need a flyer design for a product that we are a selling, a sacred Islamic cloth called a Kiswah, which is draped around the holy Kaaba in mecca every year.

The details we would like on the flyer are as follows:

Rare Kiswah of the holy Kaaba for sale (fitted in 1977 and 1982 vintage). For sale:

1) whole piece 15 meters x 2.60 meters : £60,000
2) 8 meters x 2.60 meters : £31,200
3) 4 meters x 2.60 meters : £15,600
4) 1 meter : £1500

(insert a high quality picture of holy Kaaba here, then underneath the picture, write the following:) "The Kaaba is covered by an expensive black cloth which is known as 'Kiswah' which is produced and changed every year"

(insert picture of our product here,i.e. use the document named MAIN IMAGE then underneath this picture write the following:) "Silk lampas weave Kiswah, woven silk on a black satin ground with Quranic calligraphy, the zig-zag bands of inscription alternate with the Shahadah and the inscription, 'God, exalted be His Glory!"

insert another picture of kiswah which i provided anywhere you like

(somewhere on flyer write the following) please note a percentage of sales will go towards Sadaqah for our Muslim brothers and sisters in need around the world

(somewhere on flyer write the following) Hallorand's international auction house authenticity document also available to prove the Kiswah is genuine.

100% genuine

contact us today! deals this good don't last forever.

email: relicoffer@tarnwickmail.com

Please use the images that I have attached on the flyer accordingly. Also feel free to be as creative as possible I want it to attract a lot of attention but also look professional so you may add some things to improve the look of the flyer.

note: the product being sold is on the pictures I've provided, in particular, i want file 2 "main image" in a large size on the flyer!

thank you! and happy holidays

Muslims and Islamic collectors

House

• the dimensions of the flyer is :
• A5 horizontal or vertical
• (210 x 148 mm)
• must have colors! up to you what colors to choose!

```html
<!DOCTYPE html>
<html lang="en">
<head>
<meta charset="utf-8">
<title>Rare Kiswah of the Holy Kaaba – For Sale</title>
<link rel="stylesheet" href="https://fonts.googleapis.com/css2?family=Parisienne&family=Londrina+Solid:wght@400;900&family=Bellefair&family=Rye&display=swap">
<style>
  :root {
    --cream: #fdf8d9;
    --cloth: #3a3d3f;
    --cloth-dark: #2a2c2e;
    --gold: #c9a76a;
    --brick: #a15a4c;
    --brick-text: #9c5a4b;
    --ink: #3b3431;
    --frame: #8c7d62;
    --stamp-blue: #3f5c86;
    --white: #ffffff;
  }
  * { box-sizing: border-box; margin: 0; padding: 0; }
  html, body { width: 846px; height: 1200px; overflow: hidden; background: var(--cream); }
  .flyer { position: relative; width: 846px; height: 1200px; background: var(--cream); overflow: hidden; font-family: "Bellefair", serif; color: var(--ink); }

  .header-art { position: absolute; left: 0; top: 0; width: 846px; height: 300px; }

  .title-badge { position: absolute; left: 188px; top: 28px; width: 476px; height: 320px; }
  .title-text { position: absolute; left: 188px; top: 95px; width: 476px; text-align: center; color: var(--white); }
  .title-script { font-family: "Parisienne", cursive; font-size: 58px; line-height: 58px; }
  .title-script.small { font-size: 46px; line-height: 52px; }
  .title-sale { font-family: "Londrina Solid", sans-serif; font-weight: 900; font-size: 66px; line-height: 76px; letter-spacing: 1px; }

  .vintage-stamp { position: absolute; left: 648px; top: 48px; width: 142px; height: 142px; background: #f4f1e8; border: 2px dashed #9b9280; outline: 5px solid #f4f1e8; display: flex; flex-direction: column; align-items: center; justify-content: center; color: #807560; text-align: center; }
  .vintage-stamp .small { font-family: "Bellefair", serif; font-size: 13px; letter-spacing: 1px; }
  .vintage-stamp .years { font-family: "Rye", serif; font-size: 22px; line-height: 24px; }
  .vintage-stamp .word { font-family: "Rye", serif; font-size: 30px; line-height: 34px; }

  .sale-heading { position: absolute; left: 104px; top: 370px; font-family: "Londrina Solid", sans-serif; font-size: 32px; color: var(--brick-text); letter-spacing: 1px; }
  .rule { position: absolute; left: 36px; width: 372px; height: 2px; background: var(--brick); }
  .rule::after { content: ""; position: absolute; left: 182px; top: -4px; width: 8px; height: 8px; background: var(--brick); transform: rotate(45deg); }
  .price-list { position: absolute; left: 20px; top: 440px; width: 404px; text-align: center; list-style: none; color: var(--brick-text); font-size: 25px; }
  .price-list li { line-height: 28px; margin-bottom: 22px; }
  .price-list li:first-child { margin-bottom: 18px; }

  .photo-frame { position: absolute; left: 441px; width: 379px; border: 2px solid var(--frame); background: var(--cream); padding: 9px; }
  .photo-frame .photo { width: 100%; height: 100%; }
  .kaaba-frame { top: 390px; height: 262px; }
  .kaaba-photo { background: linear-gradient(180deg, #2d6fc0 0%, #6c9ccb 45%, #c9b79a 60%, #1a1a1a 62%, #2a2622 85%, #e9e6e0 100%); }
  .cloth-frame { top: 755px; height: 265px; }
  .cloth-photo { background: radial-gradient(ellipse at 40% 40%, #3a3b3d 0%, #232426 60%, #17181a 100%); }

  .caption { position: absolute; left: 441px; width: 379px; text-align: center; font-size: 16px; line-height: 21px; color: var(--ink); }
  .kaaba-caption { top: 664px; }
  .cloth-caption { top: 1030px; }

  .sadaqah-note { position: absolute; left: 34px; top: 760px; width: 370px; font-size: 17px; line-height: 22px; }
  .auction-name { position: absolute; left: 34px; top: 860px; display: flex; align-items: center; gap: 10px; font-size: 28px; color: var(--ink); }
  .auction-name .dot { width: 14px; height: 14px; border-radius: 50%; background: var(--ink); }
  .auction-note { position: absolute; left: 34px; top: 928px; width: 320px; font-size: 17px; line-height: 22px; }
  .genuine-seal { position: absolute; left: 342px; top: 872px; width: 142px; height: 142px; }

  .contact-heading { position: absolute; left: 34px; top: 1036px; font-family: "Londrina Solid", sans-serif; font-size: 38px; color: var(--ink); letter-spacing: 1px; }
  .contact-tag { position: absolute; left: 34px; top: 1082px; font-family: Arial, Helvetica, sans-serif; font-weight: 700; font-size: 20px; color: var(--ink); }
  .dotted { position: absolute; left: 34px; width: 378px; border-top: 4px dotted var(--brick); }
  .contact-email { position: absolute; left: 34px; top: 1128px; font-family: Arial, Helvetica, sans-serif; font-weight: 700; font-size: 21px; color: var(--brick-text); }
</style>
</head>
<body>
<main class="flyer">
  <svg class="header-art" viewBox="0 0 846 300" aria-hidden="true">
    <path d="M0 0 H846 V150 C700 190 560 230 380 250 C220 268 90 262 0 255 Z" fill="var(--cloth)"/>
    <path d="M0 255 C90 262 220 268 380 250 C560 230 700 190 846 150 V185 C700 220 560 258 380 276 C220 292 90 288 0 282 Z" fill="var(--gold)"/>
    <path d="M0 282 C90 288 220 292 380 276 C560 258 700 220 846 185 V300 H0 Z" fill="var(--cream)"/>
  </svg>
  <div role="img" aria-label="Close-up of black kiswah cloth with woven calligraphy" style="position:absolute;left:0;top:0;width:0;height:0"></div>

  <svg class="title-badge" viewBox="0 0 476 320" aria-hidden="true">
    <rect x="6" y="6" width="464" height="308" rx="60" fill="var(--brick)"/>
    <rect x="24" y="24" width="428" height="272" rx="46" fill="none" stroke="var(--white)" stroke-width="3" stroke-dasharray="2 9" stroke-linecap="round"/>
  </svg>
  <h1 class="title-text">
    <div class="title-script">Rare Kiswah</div>
    <div class="title-script small">Of The Holy Kaaba</div>
    <div class="title-sale">FOR SALE!</div>
  </h1>

  <div class="vintage-stamp">
    <span class="small">FITTED IN</span>
    <span class="years">1977 &amp; 1982</span>
    <span class="word">VINTAGE</span>
  </div>

  <h2 class="sale-heading">FOR SALE:</h2>
  <div class="rule" style="top:418px"></div>
  <ul class="price-list">
    <li>Whole Piece<br>15 Meters X 2.60 Meters : £60,000</li>
    <li>8 Meters X 2.60 Meters : £31,200</li>
    <li>4 Meters X 2.60 Meters : £15,600</li>
    <li>1 Meter : £1500</li>
  </ul>
  <div class="rule" style="top:662px"></div>

  <figure class="photo-frame kaaba-frame">
    <div class="photo kaaba-photo" role="img" aria-label="The Kaaba draped in its black kiswah inside the mosque courtyard"></div>
  </figure>
  <p class="caption kaaba-caption">“The Kaaba is covered by an expensive<br>black cloth which is known as 'Kiswah'<br>which is produced and changed every year”</p>

  <figure class="photo-frame cloth-frame">
    <div class="photo cloth-photo" role="img" aria-label="The kiswah piece for sale, black silk with woven calligraphy"></div>
  </figure>
  <p class="caption cloth-caption">Silk lampas weave Kiswah, woven silk<br>on a black satin ground with<br>Quranic calligraphy,<br>the zig-zag bands of inscription<br>alternate with the Shahadah<br>and the inscription,<br>“God, exalted be His Glory!”</p>

  <p class="sadaqah-note">Percentage of sales will go towards sadaqah for our moslem brothers and sisters in need around the world.</p>

  <div class="auction-name"><span class="dot"></span>Hallorand's</div>
  <p class="auction-note">Hallorand's International Auction House authenticity document also available to prove the Kiswah is genuine.</p>

  <svg class="genuine-seal" viewBox="0 0 142 142" aria-hidden="true">
    <circle cx="71" cy="71" r="66" fill="var(--white)" stroke="var(--stamp-blue)" stroke-width="6"/>
    <circle cx="71" cy="71" r="40" fill="none" stroke="var(--stamp-blue)" stroke-width="3"/>
  </svg>

  <h2 class="contact-heading">CONTACT US TODAY!</h2>
  <p class="contact-tag">Deals this good don't last forever.</p>
  <div class="dotted" style="top:1114px"></div>
  <p class="contact-email">email: relicoffer@tarnwickmail.com</p>
  <div class="dotted" style="top:1166px"></div>
</main>
</body>
</html>
```